Meridale Leisure Company (MLC)

We need a business card design for Meridale Leisure Company. Modern and sleek looking, with all critical information. Open to single or double sided designs, if double sided info needs to be all on one side. The main Logo is Meridale Leisure company and must be on the card. The other three logos are for the brands that fall under the group, they might be good on the back.

Industry/Entity Type

Business

```html
<!DOCTYPE html>
<html lang="en">
<head>
<meta charset="utf-8">
<title>Meridale Leisure Company – Business Card</title>
<link href="https://fonts.googleapis.com/css2?family=Montserrat:wght@500;600;700&display=swap" rel="stylesheet">
<style>
  :root {
    --bg: #3a3a3a;
    --card: #ffffff;
    --blue: #2b58a6;
    --green: #8aab3a;
    --ink: #2b2b2b;
  }
  * { box-sizing: border-box; margin: 0; padding: 0; }
  html, body {
    width: 1200px; height: 900px; overflow: hidden;
    background: var(--bg);
    font-family: "Montserrat", Arial, sans-serif;
  }
  .canvas {
    width: 1200px; height: 900px;
    display: flex; flex-direction: column; align-items: center; justify-content: center;
    gap: 40px;
  }
  .card {
    position: relative;
    width: 700px; height: 400px;
    background: var(--card);
    box-shadow: 0 8px 24px rgba(0,0,0,.35);
  }

  /* Front */
  .front-logo {
    position: absolute; left: 0; right: 0; top: 120px;
    display: flex; align-items: center; justify-content: center; gap: 14px;
  }
  .mark-square { width: 34px; height: 34px; background: var(--blue); }
  .wordmark {
    color: var(--blue); font-weight: 700; font-size: 30px; letter-spacing: .5px;
    text-transform: uppercase; line-height: 1;
  }
  .brands {
    position: absolute; left: 50px; right: 50px; top: 275px;
    display: flex; justify-content: space-between; align-items: center;
  }
  .brand {
    display: flex; align-items: center; gap: 8px;
    font-weight: 700; font-size: 18px; line-height: 1;
  }
  .brand-dot { width: 16px; height: 16px; border-radius: 50%; }
  .brand--tickets { color: var(--green); }
  .brand--tickets .brand-dot { background: var(--green); }
  .brand--hospitality { color: var(--ink); }
  .brand--hospitality .brand-dot { background: var(--ink); }
  .brand--seatline { color: var(--blue); }
  .brand--seatline .brand-dot { background: var(--blue); }

  /* Back */
  .back-logo {
    position: absolute; left: 50px; top: 150px; width: 300px;
    display: flex; align-items: center; gap: 12px;
  }
  .back-logo .mark-square { width: 26px; height: 26px; flex: none; }
  .back-logo .wordmark { font-size: 21px; }
  .divider {
    position: absolute; left: 378px; top: 95px;
    width: 2px; height: 130px; background: var(--blue);
  }
  .contact { position: absolute; left: 408px; top: 90px; }
  .person-name {
    color: var(--blue); font-weight: 600; font-size: 19px; text-transform: uppercase; letter-spacing: .5px;
  }
  .person-role {
    color: var(--green); font-weight: 600; font-size: 13px; text-transform: uppercase;
    letter-spacing: .6px; margin: 2px 0 0 10px;
  }
  .contact-list { list-style: none; margin: 16px 0 0 20px; }
  .contact-list li {
    display: flex; align-items: center; gap: 10px;
    color: var(--blue); font-weight: 500; font-size: 15px; line-height: 1; margin-bottom: 7px;
  }
  .contact-icon { width: 16px; height: 16px; flex: none; }
  .address {
    position: absolute; left: 50px; bottom: 60px;
    color: var(--blue); font-weight: 600; font-size: 15px;
  }
</style>
</head>
<body>
<main class="canvas">
  <section class="card card--front" aria-label="Card front">
    <div class="front-logo">
      <span class="mark-square"></span>
      <span class="wordmark">Meridale Leisure Company</span>
    </div>
    <div class="brands">
      <div class="brand brand--tickets"><span class="brand-dot"></span>Meridale Tickets</div>
      <div class="brand brand--hospitality"><span class="brand-dot"></span>Fieldhouse Hospitality</div>
      <div class="brand brand--seatline"><span class="brand-dot"></span>seatline</div>
    </div>
  </section>

  <section class="card card--back" aria-label="Card back">
    <div class="back-logo">
      <span class="mark-square"></span>
      <span class="wordmark">Meridale Leisure Company</span>
    </div>
    <div class="divider"></div>
    <div class="contact">
      <p class="person-name">Daniel Harrow</p>
      <p class="person-role">Managing Director</p>
      <ul class="contact-list">
        <li>
          <svg class="contact-icon" viewBox="0 0 16 16" aria-hidden="true">
            <rect x=".5" y=".5" width="15" height="15" rx="4" fill="none" stroke="var(--green)"/>
            <path d="M5 4.5c0 4 2.5 6.5 6.5 6.5l.5-1.6-1.8-.8-.8 1c-1.3-.6-2.2-1.5-2.8-2.8l1-.8-.8-1.8z" fill="var(--green)"/>
          </svg>
          555 010 24 68
        </li>
        <li>
          <svg class="contact-icon" viewBox="0 0 16 16" aria-hidden="true">
            <rect x=".5" y=".5" width="15" height="15" rx="4" fill="none" stroke="var(--green)"/>
            <rect x="3.5" y="5" width="9" height="6" fill="none" stroke="var(--green)"/>
            <path d="M3.5 5l4.5 3.5L12.5 5" fill="none" stroke="var(--green)"/>
          </svg>
          d.harrow@meridalelc.com
        </li>
        <li>
          <svg class="contact-icon" viewBox="0 0 16 16" aria-hidden="true">
            <rect x=".5" y=".5" width="15" height="15" rx="4" fill="none" stroke="var(--green)"/>
            <circle cx="8" cy="8" r="4.5" fill="none" stroke="var(--green)"/>
            <path d="M3.5 8h9M8 3.5c-2 2.5-2 6.5 0 9M8 3.5c2 2.5 2 6.5 0 9" fill="none" stroke="var(--green)" stroke-width=".8"/>
          </svg>
          www.meridalelc.com
        </li>
      </ul>
    </div>
    <p class="address">48 Harbor Lane, Brookfield, New York 10482</p>
  </section>
</main>
</body>
</html>
```